PLEASE READ - DESIGN for Music Cover Tunevault - DJ and Female Singer

A nice cover to be put on Tunevault.
Definitely will be on Tunevault and All Media
Name of the song: Marivella
Singer name: Tara Wolskind
DJ name: DJ Roland Kestry

Marivella definition: A desire to be in the Sun

We need eye catching icon or something that can attract people's eyes when they see it immediately. Design must be elegant. This is not some type of Club Banging Music. The singer is a romantic and sophisticated audiophile jazz acoustic recording artist. DJ is not playing in some clubs but exclusive.

Photo of singer and DJ can be on the cover OR just photo of the singer OR just an Icon wifh their names and the song name.

Avoid these colors: Pink, Purple, Silver !!
For the background color try: A mixed of Black or Gold with Elegant Yellow, Pastel Orange, or light Blue.
For name of the song and Icon color : can be of Gold or even Red or White.
Or you can try and mix it all up yourself

Icon ideas: can be a combination of letter Capital C with small B & Capital V alone or mixed with a sun logo or half of Sun. Some cool stuff.
CB is Tara Wolskind
V is for the DJ name

Target Market(s)

Young Adult, Lounge Crowd, Club Goers / Lounge Goers, Ladies, Executives, Adults, Music Industry

Industry/Entity Type

Entertainment Industry

Font styles to use
Serif

Requirements
Must have
• MARIVELLA ( song name )
• Available on Tunevault logo
• EYE CATCHING ICON or LOGO
Should not have
• Avoid this color :
• Pink, Purple, Silver, White
• Our first project was already consisting these colors, we will attach the old design of the first song but PLEASE DO NOT apply the older design to this new project :)

```html
<!DOCTYPE html>
<html lang="en">
<head>
<meta charset="utf-8">
<title>Marivella – Tara Wolskind &amp; DJ Roland Kestry</title>
<link rel="stylesheet" href="https://fonts.googleapis.com/css2?family=Josefin+Sans:ital,wght@1,700&family=Parisienne&family=Inter:wght@400;700&display=swap">
<style>
  :root {
    --sky-orange: #f26829;
    --sun-yellow: #f5d028;
    --sun-amber: #f2b52a;
    --night: #000000;
    --ink: #0b0b0b;
    --white: #ffffff;
  }
  * { box-sizing: border-box; margin: 0; padding: 0; }
  html, body { width: 1200px; height: 1200px; overflow: hidden; background: var(--night); }
  .cover {
    position: relative;
    width: 1200px;
    height: 1200px;
    overflow: hidden;
    background: var(--sky-orange);
    font-family: "Inter", Arial, sans-serif;
  }
  .sun { position: absolute; inset: 0; width: 1200px; height: 1200px; }
  .dusk {
    position: absolute;
    inset: 0;
    background: linear-gradient(to bottom,
      rgba(0,0,0,0) 0%,
      rgba(0,0,0,0) 57%,
      rgba(30,15,10,0.35) 68%,
      rgba(20,12,10,0.8) 80%,
      var(--night) 90%,
      var(--night) 100%);
  }
  .credit {
    position: absolute;
    display: flex;
    justify-content: space-between;
    color: var(--white);
    font-size: 20px;
    font-weight: 400;
    line-height: 1;
  }
  .credit span { display: block; width: 1ch; text-align: center; }
  .credit .gap { width: 3ch; }
  .credit--singer { top: 77px; left: 78px; width: 1046px; }
  .credit--dj { top: 1087px; left: 128px; width: 948px; }
  .title {
    position: absolute;
    top: 428px;
    left: 190px;
    width: 820px;
    font-family: "Josefin Sans", "Futura", sans-serif;
    font-style: italic;
    font-weight: 700;
    font-size: 132px;
    line-height: 1;
    letter-spacing: 0.16em;
    color: var(--ink);
    white-space: nowrap;
  }
  .tagline {
    position: absolute;
    top: 600px;
    left: 190px;
    width: 790px;
    font-family: "Parisienne", cursive;
    font-size: 92px;
    line-height: 1;
    color: var(--ink);
    white-space: nowrap;
  }
  .label {
    position: absolute;
    top: 980px;
    left: 0;
    width: 1200px;
    display: flex;
    flex-direction: column;
    align-items: center;
    gap: 12px;
  }
  .label__dot {
    width: 40px;
    height: 40px;
    border-radius: 50%;
    background: var(--sky-orange);
  }
  .label__name {
    color: var(--white);
    font-size: 15px;
    font-weight: 700;
    letter-spacing: 0.04em;
  }
</style>
</head>
<body>
  <main class="cover">
    <svg class="sun" viewBox="0 0 1200 1200" aria-hidden="true">
      <defs>
        <linearGradient id="sunFill" x1="0" y1="0" x2="0" y2="1">
          <stop offset="0" stop-color="#f5d028"/>
          <stop offset="0.55" stop-color="#f5cb28"/>
          <stop offset="0.75" stop-color="#f2b52a"/>
          <stop offset="1" stop-color="#e99a2c"/>
        </linearGradient>
      </defs>
      <circle cx="586" cy="584" r="474" fill="url(#sunFill)"/>
    </svg>
    <div class="dusk"></div>

    <p class="credit credit--singer" aria-label="Tara Wolskind">
      <span>T</span><span>A</span><span>R</span><span>A</span><span class="gap"></span><span>W</span><span>O</span><span>L</span><span>S</span><span>K</span><span>I</span><span>N</span><span>D</span>
    </p>

    <h1 class="title">MARIVELLA</h1>
    <p class="tagline">A desire to be in the Sun</p>

    <div class="label">
      <span class="label__dot"></span>
      <span class="label__name">SOLVANE MUSIC</span>
    </div>

    <p class="credit credit--dj" aria-label="DJ Roland Kestry">
      <span>D</span><span>J</span><span class="gap"></span><span>R</span><span>O</span><span>L</span><span>A</span><span>N</span><span>D</span><span class="gap"></span><span>K</span><span>E</span><span>S</span><span>T</span><span>R</span><span>Y</span>
    </p>
  </main>
</body>
</html>
```